Fresh Dwelling Tract Hub needs a new Landing Page

I like to get a landing page or website with 2-3 pages to help target home buyers who are looking to buy homes from builders such as TQ Estates, Vostrum, P.J. Calloway, etc. The landing page/website to be non-cluttered and be able to explain to home buyers that there are many benefits to include me as their buyer's agent when they buy a brand new home from any builders.
I may want to incorporate a short explanation video (animated) on the landing page and then for the viewer to click on a button that will take them to another page where they can search for new homes from different builders.
Target Market(s)
Home buyers looking to buy brand new home from builders such as TQ Estates, Vostrum, P.J. Calloway, etc.
Industry/Entity Type
Real Estate
Number of Pages Required
2 page
Requirements
Must have
- The landing page may have the explanation video at the bottom of the landing page (scrolled down) or there may be a CALL TO ACTION button that takes the viewer to the 2nd page to watch the explanation video. Once they watched the explanation video and are still interested, they can click on another CALL TO ACTION button that will take them to another website that they will be able to search for all the available new homes and register their contact information.
Should not have
- No clutters and no dark colors.

```html
<!DOCTYPE html>
<html lang="en">
<head>
<meta charset="utf-8">
<title>Parkside Home Walk — Find your new home</title>
<link rel="stylesheet" href="https://fonts.googleapis.com/css2?family=Nunito:wght@900&family=Raleway:wght@400;500;700;800&display=swap">
<style>
  :root {
    --brand-blue: #3b5fa0;
    --brand-brown: #5b4632;
    --ink: #2a2a2a;
    --white: #ffffff;
    --hero-shade: rgba(40, 30, 25, 0.45);
    --band-shade: rgba(50, 55, 62, 0.55);
  }
  * { box-sizing: border-box; margin: 0; padding: 0; }
  html, body { width: 926px; height: 1200px; overflow: hidden; background: var(--white); }
  body { position: relative; font-family: "Raleway", sans-serif; color: var(--ink); }
  a { text-decoration: none; }

  .hero {
    position: absolute; left: 0; top: 0; width: 926px; height: 397px;
    background: linear-gradient(100deg, #cfc4b8 0%, #a48b72 30%, #8c6c52 55%, #b59f88 75%, #7a5c44 100%);
  }
  .hero::after { content: ""; position: absolute; inset: 0; background: var(--hero-shade); }
  .hero > * { position: absolute; z-index: 1; }

  .brand {
    left: 117px; top: 16px; width: 116px; height: 62px; background: var(--white);
    display: flex; align-items: center; justify-content: center; gap: 5px;
    font-weight: 700; font-size: 11px; color: var(--brand-brown); line-height: 1.15; text-align: left;
  }
  .brand-dot { width: 10px; height: 10px; border-radius: 50%; background: var(--brand-blue); flex: none; }

  .main-nav { top: 36px; right: 116px; display: flex; gap: 34px; font-size: 8px; font-weight: 700; }
  .main-nav a { color: var(--white); }
  .main-nav a.is-active { color: #5b86d1; }

  .hero-title {
    left: 0; width: 926px; top: 144px; text-align: center;
    font-family: "Nunito", sans-serif; font-weight: 900; font-size: 28px; color: var(--white);
  }
  .hero-lead {
    left: 240px; width: 446px; top: 189px; text-align: center;
    font-size: 10.5px; line-height: 21px; color: var(--white);
  }
  .cta {
    left: 391px; top: 284px; width: 144px; height: 40px; border-radius: 6px;
    background: var(--brand-blue); border: 1px solid #dfe6f3; color: var(--white);
    font-size: 9.5px; display: flex; align-items: center; justify-content: center;
  }

  .section-title {
    position: absolute; left: 117px; padding-left: 11px; border-left: 2px solid var(--brand-blue);
    font-weight: 800; font-size: 21px; color: var(--brand-brown); height: 29px; line-height: 31px;
  }
  .about-title { top: 415px; }
  .about-sub { position: absolute; left: 128px; top: 452px; font-size: 13px; font-weight: 500; color: var(--brand-brown); }
  .about-copy { position: absolute; left: 127px; top: 498px; width: 244px; font-size: 10.4px; line-height: 17.5px; }

  .video {
    position: absolute; left: 406px; top: 503px; width: 405px; height: 232px;
    border: 1px solid #c9c9c9;
    background: radial-gradient(ellipse at 60% 60%, #4a3a2c 0%, #2d221a 60%, #1d1611 100%);
  }
  .play { position: absolute; left: 180px; top: 94px; }

  .reviews-title { top: 776px; }
  .reviews {
    position: absolute; left: 0; top: 822px; width: 926px; height: 378px;
    background: linear-gradient(110deg, #c9d2dc 0%, #e8ebee 40%, #d5d9dc 70%, #7f8a76 100%);
  }
  .reviews::after { content: ""; position: absolute; inset: 0; background: var(--band-shade); }
  .reviews > * { position: absolute; z-index: 1; }
  .quote { left: 138px; width: 650px; top: 97px; text-align: center; color: var(--white); font-size: 14px; line-height: 17px; }
  .quote cite { display: block; font-style: normal; font-size: 11.5px; margin-top: 6px; }
  .dots { left: 424px; top: 249px; display: flex; gap: 6px; }
  .dots span { width: 23px; height: 23px; border-radius: 50%; background: var(--white); }
  .dots span.is-current { background: var(--brand-blue); border: 2px solid var(--white); }

  .social { left: 116px; top: 317px; display: flex; align-items: center; gap: 14px; color: var(--white); font-size: 10px; line-height: 13px; }
  .social-square { width: 29px; height: 29px; border-radius: 5px; background: var(--white); }
  .social a { color: #6f9ae0; }
  .legal { right: 117px; top: 316px; text-align: right; color: var(--white); font-size: 10px; line-height: 21px; }
</style>
</head>
<body>
  <header class="hero" role="img" aria-label="Bright dining room with white chairs, a wooden table and a yellow throw by the window">
    <div class="brand"><span class="brand-dot"></span><span>Parkside<br>Home Walk</span></div>
    <nav class="main-nav">
      <a class="is-active" href="#about">About Us</a>
      <a href="#homes">Your New Homes</a>
      <a href="#contact">Contact Us</a>
    </nav>
    <h1 class="hero-title">We help you find your new home</h1>
    <p class="hero-lead">Lorem ipsum dolor sit amet, consectetur adipiscing elit. Suspendisse metus mi, tincidunt vel purus molestie, sodales posuere libero. Nullam eu magna suscipit turpis imperdiet aliquet vel at dui. Maecenas justo neque, tincidunt ac eleifend in, bibendum vel lorem. Duis eu mauris viverra, tristique sem eget, eleifend es</p>
    <a class="cta" href="#homes">Search for homes</a>
  </header>

  <h2 class="section-title about-title" id="about">ABOUT US</h2>
  <p class="about-sub">Are you still curious about us? Watch our video to learn more:</p>
  <p class="about-copy">Our company provides services that help you find your dream house. Lorem ipsum dolor sit amet, consectetur adipiscing elit. Suspendisse metus mi, tincidunt vel purus molestie, sodales posuere libero. Nullam eu magna suscipit turpis imperdiet aliquet vel at dui. Maecenas justo neque, tincidunt ac eleifend in, bibendum vel lorem. Duis eu mauris viverra, tristique sem eget, eleifend es</p>
  <div class="video" role="img" aria-label="Video still of a wood-panelled bedroom with a canopy bed">
    <svg class="play" width="44" height="44" viewBox="0 0 44 44" aria-hidden="true">
      <circle cx="22" cy="22" r="20" fill="none" stroke="#ffffff" stroke-width="2"/>
      <path d="M18 14 L30 22 L18 30 Z" fill="#ffffff"/>
    </svg>
  </div>

  <h2 class="section-title reviews-title">WHAT THE CUSTOMERS SAY</h2>
  <section class="reviews" role="img" aria-label="White modern house with trees under a clear sky">
    <blockquote class="quote">“We are very happy with Parkside Home Walk, they are very helpful and now we are living in our dream home. Thank you again for your perfect service!”<cite>- Sam</cite></blockquote>
    <div class="dots"><span class="is-current"></span><span></span><span></span></div>
    <div class="social" id="contact"><span class="social-square"></span><span>Connect with us on<br><a href="#">Linkwall</a></span></div>
    <div class="legal">© ParksideHomeWalk<br>Privacy Policy | Terms &amp; Conditions</div>
  </section>
</body>
</html>
```